Forest Consultant/Timber Buyer needs a clean business card

We are a forestry consulting and timber buying company. We meet with private landowners and assist them with timber management and timber harvesting. We would like a professional business card, please no clip art. logo is blue and white but would like to see a gray,silver, or some other color incorporated. Would like basic contact info. Would like to the layout to be creative and sleek but masculine.

Target Market(s)

private landowners

Industry/Entity Type

Business

Contact Information for Business Card

name,position, cell number, office number, email, website. This might be to cluttered. Basic contact info is what we are looking for.

Contact info can all be on one side with logo on the other.

Font styles to use
Serif
Sans Serif

Colors
0255a3
ffffff
aaaaaa

Requirements
Must have
• We just want it professional.
Nice to have
• Creative layout.
Should not have
• please no clip art of log trucks etc.

```html
<!DOCTYPE html>
<html lang="en">
<head>
<meta charset="utf-8">
<title>Summit Land &amp; Timber – Business Card</title>
<link rel="stylesheet" href="https://fonts.googleapis.com/css2?family=Open+Sans:wght@400;600;700&display=swap">
<style>
  :root {
    --brand-blue: #1b4f91;
    --ink: #3a3a3a;
    --card: #ffffff;
    --backdrop: #e4e4e4;
  }
  * { box-sizing: border-box; margin: 0; padding: 0; }
  html, body {
    width: 1200px;
    height: 900px;
    overflow: hidden;
  }
  body {
    position: relative;
    background: var(--backdrop);
    font-family: "Open Sans", Arial, sans-serif;
  }
  .card {
    position: absolute;
    background: var(--card);
    box-shadow: 0 4px 14px rgba(0, 0, 0, 0.12);
  }
  .card--contact {
    left: 238px;
    top: 62px;
    width: 555px;
    height: 343px;
  }
  .card--brand {
    left: 457px;
    top: 517px;
    width: 560px;
    height: 343px;
    display: flex;
    align-items: center;
    justify-content: center;
    gap: 16px;
  }
  .brand-mark {
    position: absolute;
    left: 30px;
    top: 78px;
    width: 224px;
    height: 183px;
    display: flex;
    flex-direction: column;
    align-items: center;
    justify-content: center;
    gap: 14px;
  }
  .brand-dot {
    width: 44px;
    height: 44px;
    border-radius: 50%;
    background: var(--brand-blue);
    flex: none;
  }
  .brand-name {
    color: var(--brand-blue);
    font-weight: 700;
    font-size: 21px;
    letter-spacing: 0.5px;
    text-align: center;
    line-height: 1.25;
  }
  .card--brand .brand-name {
    font-size: 30px;
    letter-spacing: 1px;
  }
  .contact {
    position: absolute;
    left: 302px;
    top: 99px;
  }
  .contact__name {
    color: var(--brand-blue);
    font-weight: 600;
    font-size: 18px;
    line-height: 24px;
  }
  .contact__role {
    color: var(--ink);
    font-size: 14.5px;
    line-height: 20px;
  }
  .contact__list {
    list-style: none;
    margin-top: 21px;
  }
  .contact__item {
    display: flex;
    align-items: center;
    color: var(--ink);
    font-size: 14.5px;
    line-height: 20px;
  }
  .contact__icon {
    width: 11px;
    height: 11px;
    margin-right: 9px;
    fill: var(--brand-blue);
    flex: none;
  }
</style>
</head>
<body>
  <section class="card card--contact">
    <div class="brand-mark">
      <span class="brand-dot"></span>
      <span class="brand-name">Summit Land &amp; Timber</span>
    </div>
    <div class="contact">
      <p class="contact__name">Daniel Carver</p>
      <p class="contact__role">Managing Director</p>
      <ul class="contact__list">
        <li class="contact__item">
          <svg class="contact__icon" viewBox="0 0 12 12" aria-hidden="true"><path d="M3 0h6a1 1 0 0 1 1 1v10a1 1 0 0 1-1 1H3a1 1 0 0 1-1-1V1a1 1 0 0 1 1-1zm0 1.5v8h6v-8z"/></svg>
          044-555 010 200
        </li>
        <li class="contact__item">
          <svg class="contact__icon" viewBox="0 0 12 12" aria-hidden="true"><path d="M2.4 0.5l2 2.2-1 1.3c.7 1.6 2 2.9 3.6 3.6l1.3-1 2.2 2-1 2.3C5 10.6 1.4 7 0.1 1.5z"/></svg>
          044-555 010 201
        </li>
        <li class="contact__item">
          <svg class="contact__icon" viewBox="0 0 12 12" aria-hidden="true"><path d="M0 2.5h12v7H0zm1 .8v.3l5 3 5-3v-.3z"/></svg>
          info@summitland.com
        </li>
        <li class="contact__item">
          <svg class="contact__icon" viewBox="0 0 12 12" aria-hidden="true"><circle cx="6" cy="6" r="5.5"/><path d="M6 1v10M1 6h10" stroke="#fff" stroke-width="1"/></svg>
          www.summitland.com
        </li>
      </ul>
    </div>
  </section>

  <section class="card card--brand">
    <span class="brand-dot"></span>
    <span class="brand-name">Summit Land &amp; Timber</span>
  </section>
</body>
</html>
```